Wall Wrap

203.75" Wide x 124.25" Tall - wall wrap graphic!
We had a designer start this project but didn't like how it ended so we are looking for something similar. I am attaching that design as well as our brand guidelines, logos and our website for inspiration. We are open to anything! We are a franchise so we want it to scream locally owned , globally known! Please look at our website for inspiration, this design will be at the front of our showroom! I will attach a photo of the wall as well as the showroom! We will want whatever design we choose to also eventually be incorporated to a vehicle wrap!

```html
<!DOCTYPE html>
<html lang="en">
<head>
<meta charset="UTF-8">
<title>Brightly Branded Murfreesboro – Wall Wrap</title>
<link rel="stylesheet" href="https://fonts.googleapis.com/css2?family=Anton&family=Oswald:wght@600;700&display=swap">
<style>
  :root {
    --page-bg: #0d1626;
    --wall-dark: #111418;
    --wall-map: #1b2a3d;
    --brand-blue: #1f8fe6;
    --brand-blue-deep: #0b5fb0;
    --brand-blue-shadow: #083d78;
    --ink-white: #ffffff;
  }
  html, body {
    margin: 0;
    padding: 0;
    width: 900px;
    height: 1200px;
    overflow: hidden;
    background: var(--page-bg);
  }
  .canvas {
    position: relative;
    width: 900px;
    height: 1200px;
    display: flex;
    align-items: center;
    justify-content: center;
  }
  .wall-wrap {
    display: block;
    width: 860px;
    height: 524px;
  }
  .tagline {
    font-family: "Oswald", sans-serif;
    font-weight: 700;
    font-size: 30px;
    letter-spacing: 6px;
    fill: var(--ink-white);
  }
  .company-line {
    font-family: "Oswald", sans-serif;
    font-weight: 700;
    font-size: 28px;
    letter-spacing: 1px;
    fill: var(--ink-white);
  }
  .established {
    font-family: "Oswald", sans-serif;
    font-weight: 600;
    font-size: 26px;
    letter-spacing: 1px;
    fill: var(--ink-white);
  }
  .city-name {
    font-family: "Anton", sans-serif;
    font-size: 118px;
    letter-spacing: 1px;
  }
  .city-face { fill: var(--ink-white); }
  .city-extrude { fill: var(--brand-blue-deep); }
  .city-extrude-dark { fill: var(--brand-blue-shadow); }
</style>
</head>
<body>
<main class="canvas">
  <svg class="wall-wrap" viewBox="0 0 860 524" xmlns="http://www.w3.org/2000/svg" aria-label="Brightly Branded Murfreesboro wall wrap">
    <defs>
      <radialGradient id="mapGlow" cx="50%" cy="50%" r="65%">
        <stop offset="0%" stop-color="#1e3047"/>
        <stop offset="100%" stop-color="#0f1419"/>
      </radialGradient>
      <linearGradient id="blueField" x1="0" y1="0" x2="1" y2="1">
        <stop offset="0%" stop-color="#2aa0f5"/>
        <stop offset="100%" stop-color="#1272c9"/>
      </linearGradient>
    </defs>

    <!-- backdrop street map area -->
    <rect class="map-backdrop" x="0" y="0" width="860" height="524" fill="url(#mapGlow)" role="img" aria-label="Faint street map of the city in dark blue tones"/>

    <!-- top corner blue field and tagline band -->
    <polygon class="corner-field" points="0,0 860,0 0,150" fill="url(#blueField)"/>
    <polygon class="tagline-band" points="0,70 560,0 860,0 860,8 0,118" fill="var(--wall-dark)"/>
    <polygon class="band-edge" points="0,118 860,8 860,14 0,124" fill="var(--ink-white)"/>
    <text class="tagline" x="40" y="96" transform="rotate(-7.3 40 96) skewX(-12)">LOCALLY OWNED</text>

    <!-- bottom corner blue field and tagline band -->
    <polygon class="corner-field" points="860,524 0,524 860,360" fill="url(#blueField)"/>
    <polygon class="band-edge" points="0,450 860,340 860,346 0,456" fill="var(--ink-white)"/>
    <polygon class="tagline-band" points="0,456 860,346 860,400 300,524 0,524" fill="var(--wall-dark)"/>
    <text class="tagline" x="540" y="420" transform="rotate(-7.3 540 420) skewX(-12)">GLOBALLY KNOWN</text>

    <!-- headline lockup -->
    <g class="headline" transform="skewX(-10)">
      <text class="company-line" x="150" y="210">BRIGHTLY BRANDED</text>
      <g class="city-name">
        <text class="city-extrude-dark" x="154" y="330">MURFREESBORO</text>
        <text class="city-extrude-dark" x="152" y="328">MURFREESBORO</text>
        <text class="city-extrude" x="150" y="326">MURFREESBORO</text>
        <text class="city-extrude" x="148" y="324">MURFREESBORO</text>
        <text class="city-face" x="144" y="320">MURFREESBORO</text>
      </g>
      <text class="established" x="660" y="362">EST 2019</text>
    </g>
  </svg>
</main>
</body>
</html>
```